Website for Foodstuff Import-Export Company *

We need a website for our company which imports and sell ( edible oil , ketchup , mayonnaise and pulses ). our current website is velmorix.pl , we need a website which has corporate appearance with good quality products.

Target Market(s)

European Wholesalers , Supermarket Chains,

Coding

Coded - Design and coding required

Number of Pages Required

1 page

```html
<!DOCTYPE html>
<html lang="en">
<head>
<meta charset="utf-8">
<title>Velmorix – Quality Products &amp; Reliable Services</title>
<link href="https://fonts.googleapis.com/css2?family=Playfair+Display:wght@700&family=Raleway:wght@300;400;500&display=swap" rel="stylesheet">
<style>
:root{
  --yellow:#ffd000;
  --yellow-dark:#e9b800;
  --slate:#464a52;
  --slate-text:#4d4f55;
  --muted:#6d6f73;
  --cream:#f6f4ef;
  --footer:#3f424a;
  --footer-text:#b9bbc0;
  --white:#ffffff;
  --line:#e2e0da;
}
*{box-sizing:border-box;margin:0;padding:0}
html,body{width:1200px;height:3256px;overflow:hidden}
body{position:relative;background:var(--white);font-family:'Raleway',sans-serif;color:var(--slate-text)}
.abs{position:absolute}
.serif{font-family:'Playfair Display',serif;font-weight:700}

/* header */
.site-header{left:0;top:0;width:1200px;height:71px;background:var(--white)}
.brand{left:160px;top:18px;display:flex;align-items:center;gap:8px;font-family:'Raleway',sans-serif;font-weight:500;font-size:17px;letter-spacing:1px;color:#2f9a7a}
.brand-mark{width:22px;height:22px;border-radius:50%;background:#2f9a7a}
.main-nav{left:346px;top:29px;display:flex;gap:41px;font-size:11.5px;letter-spacing:1.2px;color:#444;font-weight:400}
.main-nav .active{color:var(--yellow-dark)}

/* hero */
.hero{left:7px;top:71px;width:1185px;height:476px;background:radial-gradient(ellipse at 62% 30%,#c9c48a 0%,#8fa25a 35%,#6f8a43 60%,#5a6e36 100%)}
.hero-shade{left:7px;top:71px;width:1185px;height:476px;background:linear-gradient(180deg,rgba(0,0,0,.12),rgba(0,0,0,.05) 60%,rgba(140,40,40,.25))}
.hero-kicker{left:0;width:1260px;top:204px;text-align:center;color:#fff;font-weight:300;font-size:33px}
.hero-rule{left:620px;top:253px;width:26px;height:2px;background:#fff}
.hero-title{left:0;width:1260px;top:290px;text-align:center;color:#fff8e0;font-size:47px}
.btn{display:flex;align-items:center;justify-content:center;background:var(--yellow);color:#7a6400;font-size:13px;letter-spacing:.5px}
.hero-btn{left:538px;top:439px;width:133px;height:45px}

/* features band */
.feature-band{left:7px;top:547px;width:1185px;height:298px;background:var(--yellow)}
.feature{top:605px;width:210px;text-align:center}
.feature .icon{width:71px;height:71px;border-radius:50%;background:var(--slate);margin:0 auto;position:relative}
.feature .icon::after,.range-item .icon::after{content:"";position:absolute;left:50%;top:50%;width:22px;height:22px;margin:-11px;border-radius:50%;background:var(--yellow)}
.feature h3{margin-top:18px;font-size:17.5px;color:var(--slate)}
.feature .rule{width:24px;height:2px;background:var(--slate);margin:7px auto 14px}
.feature p{font-size:11px;line-height:18px;color:#5a4d10}

/* range */
.section-title{left:0;width:1200px;text-align:center;font-size:32px;color:var(--slate)}
.range-ornament{left:558px;top:900px;width:84px;height:98px;border-radius:50%;background:#f1f0ec}
.slider-tab{left:160px;top:1044px;width:36px;height:71px;background:var(--yellow)}
.slider-photo{left:196px;top:1044px;width:550px;height:269px;background:linear-gradient(120deg,#4b3a28 0%,#8a6a45 35%,#efe6c8 55%,#5f7a3a 80%,#3b2f22 100%)}
.slider-panel{left:746px;top:1044px;width:293px;height:269px;background:var(--yellow)}
.slider-panel .icon{position:absolute;left:124px;top:48px;width:44px;height:44px;border-radius:50%;background:var(--slate)}
.slider-panel p{position:absolute;left:20px;top:126px;width:253px;text-align:center;font-size:17px;line-height:23px;color:var(--slate)}

.range-item{width:290px;display:flex;gap:16px}
.range-item .icon{flex:none;width:76px;height:76px;border-radius:50%;background:#eeede9;position:relative}
.range-item .icon::after{background:#9a9b9e;width:18px;height:18px;margin:-9px}
.range-item h4{margin-top:16px;font-size:18px;color:var(--slate)}
.range-item .rule{width:24px;height:2px;background:var(--slate);margin:6px 0 10px}
.range-item p{font-size:11px;line-height:18.5px;color:var(--muted)}

/* banner */
.banner{left:8px;top:1720px;width:1184px;height:307px;background:linear-gradient(90deg,#4a3a2c 0%,#7a5c3e 30%,#6a513a 60%,#8b6a45 85%,#5a4430 100%)}
.banner-shade{left:8px;top:1720px;width:1184px;height:307px;background:rgba(40,30,25,.35)}
.banner-title{left:0;width:1200px;top:1800px;text-align:center;font-size:58px;line-height:66px;color:#fbf3e3}

/* products */
.products{left:8px;top:2027px;width:1184px;height:683px;background:var(--cream)}
.products-badge{left:563px;top:2004px;width:74px;height:74px;border-radius:50%;background:var(--white)}
.product-card{top:2167px;width:275px;height:408px;background:var(--white);border:2px solid var(--line);text-align:center}
.product-photo{margin:34px auto 0;width:180px;height:230px;border-radius:8px}
.product-card .name{margin-top:34px;font-size:10px;color:var(--muted)}
.product-card .price{margin-top:6px;font-family:'Playfair Display',serif;font-weight:700;font-size:18px;color:var(--slate)}
.product-card .rule{width:24px;height:2px;background:var(--slate);margin:6px auto 0}
.view-btn{left:546px;top:2607px;width:108px;height:45px}

/* footer */
.site-footer{left:0;top:2710px;width:1200px;height:546px;background:var(--footer)}
.footer-col{top:2812px;width:200px;color:var(--footer-text);font-size:11px;line-height:18.5px}
.footer-col h5{font-family:'Playfair Display',serif;font-weight:700;font-size:17px;color:var(--yellow);line-height:22px}
.footer-col .rule{width:24px;height:2px;background:var(--yellow);margin:8px 0 12px}
.footer-col ul{list-style:none}
.email-field{margin-top:16px;width:160px;height:38px;border:1px solid #5a5d65;padding:0 18px;display:flex;align-items:center;color:#9a9ca1}
.consent{margin-top:14px;display:flex;gap:8px;font-size:10px;line-height:17px}
.consent span{flex:none;width:12px;height:12px;background:#fff;margin-top:2px}
.subscribe{margin-top:10px;width:116px;height:30px;font-size:9.5px;color:#5a4a00}
.socials{margin-top:16px;display:flex;gap:6px}
.socials span{width:29px;height:29px;border-radius:50%;background:var(--yellow)}
.copyright{left:160px;top:3129px;font-size:11px;color:#e5e6e8}
.copyright b{color:var(--yellow);font-weight:400}
</style>
</head>
<body>

<header class="abs site-header">
  <div class="abs brand"><span class="brand-mark"></span>VELMORIX</div>
  <nav class="abs main-nav">
    <span class="active">HOME</span><span>ABOUT US</span><span>PRODUCTS</span><span>CSR</span><span>NEWS</span><span>CONTACT US</span>
  </nav>
</header>

<section>
  <div class="abs hero" role="img" aria-label="Olive oil pouring over a fresh salad"></div>
  <div class="abs hero-shade"></div>
  <p class="abs hero-kicker">High quality oil, ketchup , mayonnaise and pulses</p>
  <div class="abs hero-rule"></div>
  <h1 class="abs hero-title serif">Quality Products &amp; Reliable Services</h1>
  <a class="abs btn hero-btn">ORDER NOW!</a>
</section>

<section>
  <div class="abs feature-band"></div>
  <div class="abs feature" style="left:154px">
    <div class="icon" role="img" aria-label="Olive branch icon"></div>
    <h3 class="serif">Gourmet Flavour</h3><div class="rule"></div>
    <p>We focus on providing our clients only the freshest products from around the world.</p>
  </div>
  <div class="abs feature" style="left:381px">
    <div class="icon" role="img" aria-label="Oil jar icon"></div>
    <h3 class="serif">Special Oils</h3><div class="rule"></div>
    <p>The taste, the aroma and the natural ingredients of our products are kept unaltered.</p>
  </div>
  <div class="abs feature" style="left:607px">
    <div class="icon" role="img" aria-label="Olive drop icon"></div>
    <h3 class="serif">Health Benefits</h3><div class="rule"></div>
    <p>The health benefits of our oil are unrivaled, and research reveals new every day.</p>
  </div>
  <div class="abs feature" style="left:833px">
    <div class="icon" role="img" aria-label="Oil bottle and olive icon"></div>
    <h3 class="serif">Extraordinary Taste</h3><div class="rule"></div>
    <p>We produce every day the extraordinary just-pressed organic taste.</p>
  </div>
</section>

<section>
  <div class="abs range-ornament" role="img" aria-label="Faint olive wreath ornament"></div>
  <h2 class="abs section-title serif" style="top:928px">Our Range</h2>

  <div class="abs slider-tab">
    <svg width="36" height="71" viewBox="0 0 36 71"><path d="M20 12l-5 5 5 5M16 44l5 5-5 5" fill="none" stroke="#7a6400" stroke-width="1.5"/></svg>
  </div>
  <div class="abs slider-photo" role="img" aria-label="Bowl of mayonnaise with parsley, lemon and quail eggs"></div>
  <div class="abs slider-panel">
    <div class="icon" role="img" aria-label="Olive icon"></div>
    <p class="serif">Choose From Our Superb Range of Quality Oil, Ketchup, Mayonnaise and Pulses</p>
  </div>

  <div class="abs range-item" style="left:160px;top:1387px"><div class="icon" role="img" aria-label="Olive icon"></div><div><h4 class="serif">Extra Virgin</h4><div class="rule"></div><p>Lorem ipsum dolor sit amet, consectetur adipiscing elit, sed do eiusmod tempor.</p></div></div>
  <div class="abs range-item" style="left:462px;top:1387px"><div class="icon" role="img" aria-label="Olive tree icon"></div><div><h4 class="serif">New Harvest</h4><div class="rule"></div><p>Lorem ipsum dolor sit amet, consectetur adipiscing elit, sed do eiusmod tempor.</p></div></div>
  <div class="abs range-item" style="left:764px;top:1387px"><div class="icon" role="img" aria-label="Oil jar icon"></div><div><h4 class="serif">Original Taste</h4><div class="rule"></div><p>Lorem ipsum dolor sit amet, consectetur adipiscing elit, sed do eiusmod tempor.</p></div></div>
  <div class="abs range-item" style="left:160px;top:1531px"><div class="icon" role="img" aria-label="Olive sprig icon"></div><div><h4 class="serif">A Delicate Blend</h4><div class="rule"></div><p>Lorem ipsum dolor sit amet, consectetur adipiscing elit, sed do eiusmod tempor.</p></div></div>
  <div class="abs range-item" style="left:462px;top:1531px"><div class="icon" role="img" aria-label="Oil bottle icon"></div><div><h4 class="serif">High Quality</h4><div class="rule"></div><p>Lorem ipsum dolor sit amet, consectetur adipiscing elit, sed do eiusmod tempor.</p></div></div>
  <div class="abs range-item" style="left:764px;top:1531px"><div class="icon" role="img" aria-label="Olives icon"></div><div><h4 class="serif">Organic Only</h4><div class="rule"></div><p>Lorem ipsum dolor sit amet, consectetur adipiscing elit, sed do eiusmod tempor.</p></div></div>
</section>

<section>
  <div class="abs banner" role="img" aria-label="Burlap sacks of olives at harvest"></div>
  <div class="abs banner-shade"></div>
  <h2 class="abs banner-title serif">The poetry of olives for heartfelt<br>culinary inspiration</h2>
</section>

<section>
  <div class="abs products"></div>
  <div class="abs products-badge" role="img" aria-label="Olive branch badge"></div>
  <h2 class="abs section-title serif" style="top:2055px">Products</h2>

  <div class="abs product-card" style="left:160px">
    <div class="product-photo" role="img" aria-label="Canister of sunflower oil" style="background:linear-gradient(180deg,#f3d35a,#e8b420 60%,#f0c94a)"></div>
    <p class="name">Oil</p><p class="price">$40.99</p><div class="rule"></div>
  </div>
  <div class="abs product-card" style="left:463px">
    <div class="product-photo" role="img" aria-label="Bucket of ketchup" style="background:linear-gradient(180deg,#c8202a 0%,#d84a3a 30%,#f4f0ea 55%,#e0b23a 100%)"></div>
    <p class="name">Ketchup</p><p class="price">$12.99</p><div class="rule"></div>
  </div>
  <div class="abs product-card" style="left:764px">
    <div class="product-photo" role="img" aria-label="Bucket of mayonnaise" style="background:linear-gradient(180deg,#c9a27a 0%,#e9dccb 30%,#f6f2ea 60%,#e8e2d6 100%)"></div>
    <p class="name">Mayonnaise</p><p class="price">$28.99</p><div class="rule"></div>
  </div>

  <a class="abs btn view-btn">VIEW ALL</a>
</section>

<footer class="abs site-footer"></footer>
<div class="abs footer-col" style="left:160px">
  <h5>About Us</h5><div class="rule"></div>
  <p>VELMORIX is a manufacturing and trading company in Wrocław , Poland We established longer and closer working relationships with our clients and supplier not only provide immediate and reliable service but to continually exceed expectations and goals.</p>
</div>
<div class="abs footer-col" style="left:387px">
  <h5>Information</h5><div class="rule"></div>
  <ul><li>Home</li><li>Our Range</li><li>About Us</li><li>News</li><li>Contacts</li></ul>
</div>
<div class="abs footer-col" style="left:613px">
  <h5>Newsletter</h5><div class="rule"></div>
  <p>Stay up to date with all our recent products and promotions</p>
  <div class="email-field">Your Email</div>
  <div class="consent"><span></span>I have read and agree to the terms &amp; conditions</div>
  <div class="btn subscribe">SUBSCRIBE</div>
</div>
<div class="abs footer-col" style="left:840px">
  <h5>Contact us</h5><div class="rule"></div>
  <p>ul. Lipowa 18 /4c<br>50-118, Wrocław Polska</p>
  <p style="margin-top:18px">Phone: +48700123456<br>Email: info@velmorix.pl</p>
  <div class="socials"><span></span><span></span></div>
</div>
<p class="abs copyright"><b>Velmorix</b> © 2020. All rights reserved.</p>

</body>
</html>
```